Willowmere Loft B&B Business Card

This beautiful high-class B&B is looking for a business card that stands out from the rest. They are in the middle of the countryside, have chickens, geese and a dog. They also love bumble bees.

I was maybe thinking a rustic drawing / print of a bumble bee and a sketch of the house, I am not sure.. I quite like the feel of this... http://www.tarnwick-mill.co.uk/

Industry/Entity Type

Business

Contact Information for Business Card

Willowmere Loft
Bed & Breakfast
Brackleford, Hensworth, Somerset, TA14 7QP
01632 960418 | www.willowmereloft.co.uk

```html
<!DOCTYPE html>
<html lang="en">
<head>
<meta charset="utf-8">
<title>Willowmere Loft B&amp;B Business Card</title>
<link rel="stylesheet" href="https://fonts.googleapis.com/css2?family=Open+Sans:wght@400;600&display=swap">
<style>
  :root {
    --ink: #3a2418;
    --card: #ffffff;
    --backdrop: #ece7e1;
  }
  * { margin: 0; padding: 0; box-sizing: border-box; }
  html, body {
    width: 1200px;
    height: 1000px;
    overflow: hidden;
    background: var(--backdrop);
    font-family: "Open Sans", Arial, sans-serif;
    color: var(--ink);
  }
  .business-card {
    position: absolute;
    left: 150px;
    top: 232px;
    width: 900px;
    height: 536px;
    background: var(--card);
    box-shadow: 0 6px 18px rgba(0, 0, 0, 0.18);
  }
  .contact-block {
    position: absolute;
    left: 45px;
    top: 140px;
  }
  .business-name {
    font-size: 28px;
    font-weight: 600;
    letter-spacing: 0.2px;
    margin-bottom: 38px;
  }
  .detail {
    font-size: 20px;
    line-height: 31px;
  }
  .tagline { margin-bottom: 12px; }
  .address { margin-bottom: 14px; }
  .contact-line {
    display: flex;
    align-items: center;
    gap: 10px;
  }
  .contact-line svg {
    width: 16px;
    height: 16px;
    fill: var(--ink);
    flex: none;
  }
  .brand-mark {
    position: absolute;
    left: 413px;
    top: 127px;
    width: 442px;
    height: 283px;
    display: flex;
    align-items: center;
    justify-content: center;
    gap: 18px;
  }
  .brand-dot {
    align-self: flex-start;
    margin-top: 42px;
    width: 30px;
    height: 30px;
    border-radius: 50%;
    background: var(--ink);
    flex: none;
  }
  .brand-name {
    display: flex;
    flex-direction: column;
    font-size: 64px;
    line-height: 76px;
    font-weight: 600;
    color: var(--ink);
    white-space: nowrap;
  }
  .brand-name .second-line { align-self: flex-end; }
</style>
</head>
<body>
  <section class="business-card">
    <div class="contact-block">
      <h1 class="business-name">WILLOWMERE LOFT</h1>
      <p class="detail tagline">Bed &amp; Breakfast</p>
      <p class="detail address">Brackleford, Hensworth,<br>Somerset, TA14 7QP</p>
      <p class="detail contact-line">
        <svg viewBox="0 0 16 16" aria-hidden="true">
          <path d="M1 6c0-2 3-3.5 7-3.5S15 4 15 6v1.2h-3.4V5.6C10.6 5.2 9.3 5 8 5s-2.6.2-3.6.6v1.6H1z"/>
          <path d="M4 8.2h8l2 5.3H2z"/>
        </svg>
        01632 960418
      </p>
      <p class="detail contact-line">
        <svg viewBox="0 0 16 16" aria-hidden="true">
          <path d="M1 3.5h14L8 9z"/>
          <path d="M1 4v8.5h14V4L8 9.5z"/>
        </svg>
        www.willowmereloft.co.uk
      </p>
    </div>
    <div class="brand-mark">
      <span class="brand-dot" aria-hidden="true"></span>
      <span class="brand-name"><span>Willowmere</span><span class="second-line">Loft</span></span>
    </div>
  </section>
</body>
</html>
```